Need a image for a Chirpwall ad campaign

Need a image designed for a Chirpwall ad campaign. We are setting up a Chirpwall campaign advertising on Chirpwall for people who would want to get into modelling. We accept people aged 4+ . We want them to go to glowrunwayhub dot com to sign up and apply. We need this image to comply with Chirpwall ad policies. It can't have more than 20% text on it.

Maybe just say Become a Model or something
Glow Runway Hub or something your choice.

What size should my ad image be?

The best image size to use for your ad depends on what type of ad you're creating, but a best practice is to size your images to be 1200 x 628 pixels. The Promo Spec Handbook contains all of the specifications around the recommended ad image sizes for each ad type. If your image is larger or smaller than the dimensions specified in the Promo Spec Handbook, it will be automatically resized to fit in the ad. Animated or flash images aren't supported.

Keep in mind that your ad may not contain more than 20% text in the ad's image.

People who would want to get into modelling

Advertising

Sans Serif

Designer to choose colors to be used in the design.

Must have
• Must tie in with the main website glowrunwayhub dot com

```html
<!DOCTYPE html>
<html lang="en">
<head>
<meta charset="UTF-8">
<title>Glow Runway Hub – Become a Model</title>
<link rel="stylesheet" href="https://fonts.googleapis.com/css2?family=Roboto+Condensed:wght@700&family=Playfair+Display:wght@400&family=Cormorant+Garamond:wght@500&display=swap">
<style>
  :root {
    --bg-deep: #1c1916;
    --bg-warm: #4a423b;
    --bg-mid: #35302b;
    --bg-light: #8a8178;
    --tan: #caa47c;
    --banner: #7d6853;
    --banner-text: #efe3d3;
    --headline: #ffffff;
    --tagline: #e6e0d8;
    --rule: rgba(255, 255, 255, 0.35);
  }
  * { margin: 0; padding: 0; box-sizing: border-box; }
  html, body { width: 1200px; height: 628px; overflow: hidden; background: var(--bg-deep); }
  .ad {
    position: relative;
    width: 1200px;
    height: 628px;
    overflow: hidden;
  }
  .ad-photo {
    position: absolute;
    inset: 0;
    background:
      radial-gradient(ellipse 420px 360px at 200px 260px, rgba(120, 108, 96, 0.55), transparent 70%),
      radial-gradient(ellipse 300px 260px at 1080px 200px, rgba(150, 140, 128, 0.45), transparent 70%),
      radial-gradient(ellipse 260px 220px at 1040px 300px, rgba(20, 16, 14, 0.9), transparent 75%),
      radial-gradient(ellipse 600px 200px at 700px 600px, rgba(90, 82, 74, 0.45), transparent 70%),
      linear-gradient(100deg, var(--bg-warm) 0%, var(--bg-mid) 45%, var(--bg-deep) 100%);
  }
  .intro {
    position: absolute;
    left: 48px;
    top: 168px;
    font-family: "Roboto Condensed", "Arial Narrow", sans-serif;
    font-weight: 700;
    font-size: 37px;
    line-height: 56px;
    color: var(--tan);
  }
  .register {
    position: absolute;
    left: 0;
    top: 320px;
    width: 378px;
    height: 64px;
  }
  .register svg { position: absolute; inset: 0; }
  .register-label {
    position: absolute;
    left: 48px;
    top: 0;
    line-height: 64px;
    font-family: "Roboto Condensed", "Arial Narrow", sans-serif;
    font-weight: 700;
    font-size: 25px;
    color: var(--banner-text);
    letter-spacing: 0.3px;
  }
  .brand-block {
    position: absolute;
    left: 505px;
    top: 128px;
    width: 665px;
    height: 400px;
  }
  .rule {
    position: absolute;
    left: 0;
    width: 665px;
    height: 6px;
    border-top: 1px dotted var(--rule);
    border-bottom: 1px dotted var(--rule);
  }
  .rule-top { top: 2px; }
  .rule-bottom { top: 330px; }
  .brand-name {
    position: absolute;
    left: 0;
    top: 30px;
    width: 720px;
    text-align: center;
    font-family: "Playfair Display", "Times New Roman", serif;
    color: var(--headline);
    text-transform: uppercase;
  }
  .brand-name .big {
    display: block;
    font-size: 118px;
    line-height: 112px;
    letter-spacing: 2px;
  }
  .brand-name .small {
    display: block;
    font-size: 48px;
    line-height: 64px;
  }
  .tagline {
    position: absolute;
    left: 35px;
    top: 368px;
    width: 630px;
    text-align: center;
    font-family: "Cormorant Garamond", "Times New Roman", serif;
    font-weight: 500;
    font-size: 16px;
    letter-spacing: 6.3px;
    color: var(--tagline);
    text-transform: uppercase;
  }
</style>
</head>
<body>
  <div class="ad">
    <div class="ad-photo" role="img" aria-label="Soft sepia photograph of a young child's face on the left blending into a vintage camera lens on the right"></div>

    <p class="intro">Do you want become<br>a Model?</p>

    <div class="register">
      <svg width="378" height="64" viewBox="0 0 378 64" aria-hidden="true">
        <polygon points="0,0 348,0 378,32 348,64 0,64" fill="var(--banner)"/>
      </svg>
      <span class="register-label">REGISTER YOURSELF</span>
    </div>

    <div class="brand-block">
      <div class="rule rule-top"></div>
      <h1 class="brand-name">
        <span class="big">Glow</span>
        <span class="small">Runway</span>
        <span class="big">Hub</span>
      </h1>
      <div class="rule rule-bottom"></div>
      <p class="tagline">Platform for aspiring models</p>
    </div>
  </div>
</body>
</html>
```